Simple Website Design for Law Office

I need a website design for our law office (Law Offices of Marcus Pellow) that is extremely simple, only including a landing page and perhaps a contact page (parallax scrolling).

Website should look similar to this one (template): https://www.brightfenwaystudio.com/

Design should be modern, simple, and inviting. There are a few assets like logo, stock photos/icons we would like added as well, and some language and contact info, but very basic stuff.

The name of the company is: Law Offices of Marcus Pellow

Target Market(s)

B2B corporate clients, users from Canada, UK, East Asia, and all potential users with immigration needs

Coding

Coded - Design and coding required

Number of Pages Required

2 page

Colors

Designer to choose colors to be used in the design.

Requirements
Must have
• Landing page, Contact Page
• Simple, elegant design with minimalist font
Nice to have
• Parallax scrolling, so one page and can scroll to contact us segment

```html
<!DOCTYPE html>
<html lang="en">
<head>
<meta charset="utf-8">
<title>Law Offices of Marcus Pellow</title>
<link rel="stylesheet" href="https://fonts.googleapis.com/css2?family=Playfair+Display:wght@700;900&family=Poppins:wght@400;500;600&display=swap">
<style>
:root{
  --red:#e8333c;
  --crimson:#c4121a;
  --dark-red:#9b0a10;
  --ink:#222;
  --muted:#6d6d6d;
  --paper:#f9f9f6;
  --black:#0d0d0d;
  --navy:#17178a;
  --white:#fff;
  --serif:'Playfair Display', Georgia, serif;
  --sans:'Poppins', Arial, sans-serif;
}
*{margin:0;padding:0;box-sizing:border-box}
html,body{width:708px;height:1200px;overflow:hidden}
body{position:relative;background:var(--white);font-family:var(--sans);color:var(--ink)}
.abs{position:absolute}

.topbar{left:0;top:0;width:708px;height:14px;background:var(--red);color:var(--white);font-size:6px;display:flex;justify-content:flex-end;align-items:center;gap:14px;padding-right:142px}
.topbar span{display:flex;align-items:center;gap:4px}

.header{left:0;top:14px;width:708px;height:52px;background:var(--white)}
.brand{left:140px;top:13px;color:var(--crimson);font-family:var(--serif)}
.brand-pre{font-size:8px;font-weight:700;color:#333;margin-left:18px;line-height:1}
.brand-name{font-size:14.5px;font-weight:900;letter-spacing:.5px;line-height:1.2}
.nav{top:23px;left:0;width:708px;font-size:6.6px;font-weight:500;color:#111}
.nav a{position:absolute;color:inherit;text-decoration:none;white-space:nowrap}
.nav a.active{color:#2a2a9a}
.nav a.active::after{content:"";position:absolute;left:0;right:0;top:12px;height:2px;background:var(--crimson)}

.hero{left:0;top:66px;width:708px;height:272px;background:linear-gradient(160deg,#3c4f5e 0%,#2b3e4f 45%,#4d5f68 80%,#6b6b5a 100%)}
.hero-title{left:154px;top:180px;font-family:var(--serif);font-size:27px;font-weight:700;letter-spacing:2.5px;color:var(--white)}
.hero-sub{left:154px;top:217px;font-size:10.5px;font-weight:500;letter-spacing:.8px;color:var(--white)}
.hero-btn{left:159px;top:250px;width:99px;height:20px;background:var(--white);color:#222;font-size:6.6px;font-weight:500;letter-spacing:1.6px;display:flex;align-items:center;justify-content:center}
.hero-cut{left:0;top:260px}

.share{left:0;top:114px;width:17px}
.share div{width:17px;height:17.6px;display:flex;align-items:center;justify-content:center}

.about-bg{left:0;top:338px;width:708px;height:210px;background:var(--paper)}
.h-section{font-family:var(--serif);font-weight:700;font-size:14px;letter-spacing:.8px;color:#1b1b1b}
.rule{width:14px;height:2px;background:#1b1b1b}
.about-title{left:140px;top:351px}
.about-rule{left:140px;top:372px}
.about-tag{left:140px;top:389px;font-size:6.4px;color:var(--muted)}
.about-copy{left:140px;width:232px;font-size:6.4px;line-height:10.4px;color:var(--muted)}
.btn-red{left:140px;top:506px;width:98px;height:20px;background:var(--crimson);color:var(--white);font-size:6.6px;display:flex;align-items:center;justify-content:center}

.practice{left:0;top:546px}
.practice-title{left:0;top:596px;width:708px;text-align:center;color:var(--white)}
.practice-rule{left:347px;top:617px;background:var(--white)}
.area{top:642px;width:120px;text-align:center;color:var(--white);font-size:7px;font-weight:500;letter-spacing:.3px}
.area svg{display:block;margin:0 auto 8px}
.dots{left:318px;top:722px;display:flex;gap:4px}
.dots i{width:10px;height:2px;background:var(--white)}
.dots i.on{background:#5a9bd6}

.portrait{left:400px;top:348px;width:124px;height:220px;border-radius:50px 50px 0 0;background:linear-gradient(180deg,#e9e4dd 0%,#2a2a2e 40%,#15151a 100%)}

.team-title{left:0;top:785px;width:708px;text-align:center}
.team-rule{left:347px;top:809px}
.card{top:829px;width:96px;height:142px;background:var(--white);border-top:2px solid var(--crimson);border-bottom:2px solid var(--crimson);box-shadow:0 1px 4px rgba(0,0,0,.25);text-align:center}
.card-photo{height:100px;background:linear-gradient(160deg,#b9bfc4,#4c5660)}
.card-name{margin-top:9px;font-size:6.3px;font-weight:600;color:#111}
.card-role{font-size:5.6px;color:#444;line-height:7px;margin-top:1px}
.arrow{top:891px;width:18px;height:18px;border-radius:50%;background:var(--crimson);display:flex;align-items:center;justify-content:center}

.foot-info{left:0;top:1002px;width:287px;height:176px;background:var(--black);color:var(--white)}
.foot-info .office{position:absolute;left:138px;top:8px;font-size:8px;font-weight:600;letter-spacing:.3px}
.foot-info dl{position:absolute;left:138px;top:28px;font-size:6px;line-height:8.5px}
.foot-info dt{color:var(--red);font-weight:500}
.foot-info dd{margin-bottom:9px}
.foot-social{position:absolute;left:140px;top:148px;display:flex;gap:3px}
.foot-social i{width:12px;height:12px;display:block}

.contact{left:287px;top:1002px;width:135px;height:176px;background:var(--crimson);color:var(--white)}
.contact h2{position:absolute;left:17px;top:8px;font-family:var(--serif);font-size:14px;font-weight:700}
.field{position:absolute;left:16px;width:106px;font-size:5.4px;border-bottom:1px solid rgba(255,255,255,.85);padding-bottom:2px}
.submit{position:absolute;left:28px;top:146px;width:81px;height:18px;border:1px solid var(--white);font-size:6.4px;display:flex;align-items:center;justify-content:center}

.map{left:422px;top:1002px;width:286px;height:176px;background:linear-gradient(110deg,#a9d3f2 0%,#b9dcf3 18%,#ececec 30%,#e4e4e4 70%,#efefef 100%)}
.copyright{left:0;top:1178px;width:708px;height:22px;background:var(--navy);color:var(--white);font-size:5.6px;display:flex;align-items:center;justify-content:center}
</style>
</head>
<body>

<div class="abs topbar">
  <span><svg width="7" height="5" viewBox="0 0 7 5"><rect width="7" height="5" fill="#fff"/><path d="M0 0L3.5 3L7 0" stroke="#e8333c" stroke-width=".8" fill="none"/></svg>info@marcuspellow.com</span>
  <span><svg width="6" height="6" viewBox="0 0 10 10"><path d="M2 0L4 3L3 4Q4 6 6 7L7 6L10 8L8 10Q0 8 0 2Z" fill="#fff"/></svg>+1.808.555.0142</span>
</div>

<header class="abs header">
  <div class="abs brand">
    <div class="brand-pre">Law Offices of</div>
    <div class="brand-name">MARCUS PELLOW</div>
  </div>
  <nav class="abs nav">
    <a class="active" style="left:356px">HOME</a>
    <a style="left:391px">ABOUT US</a>
    <a style="left:441px">SERVICES</a>
    <a style="left:491px">LOCATIONS</a>
    <a style="left:540px">CONTACT</a>
  </nav>
</header>

<section class="abs hero" role="img" aria-label="City skyline with glass high-rise towers under a blue sky"></section>
<svg class="abs hero-cut" width="708" height="80" viewBox="0 260 708 80">
  <polygon points="0,264 244,328 708,278 708,340 0,340" fill="#f9f9f6"/>
  <polygon points="266,328 708,272 708,284 288,339" fill="#9b0a10"/>
</svg>
<div class="abs hero-title">LEGAL SOLUTIONS</div>
<div class="abs hero-sub">LET OUR EXPERIENCE BE YOUR GUIDE</div>
<div class="abs hero-btn">READ MORE</div>

<div class="abs share">
  <div style="background:#3b5a9a"></div>
  <div style="background:#2aa3e0"></div>
  <div style="background:#7a8a93"><svg width="9" height="8" viewBox="0 0 9 8"><rect x="2" y="0" width="5" height="2" fill="#fff"/><rect x="0" y="2.5" width="9" height="3.5" fill="#fff"/><rect x="2" y="5" width="5" height="3" fill="#fff" stroke="#7a8a93" stroke-width=".6"/></svg></div>
  <div style="background:#848e96"><svg width="9" height="6" viewBox="0 0 9 6"><rect width="9" height="6" fill="#fff"/><path d="M0 0L4.5 3.5L9 0" stroke="#848e96" stroke-width=".8" fill="none"/></svg></div>
  <div style="background:#f2653f"><svg width="8" height="8" viewBox="0 0 8 8"><path d="M4 0V8M0 4H8" stroke="#fff" stroke-width="2"/></svg></div>
</div>

<section class="abs about-bg"></section>
<h2 class="abs h-section about-title">ABOUT US</h2>
<div class="abs rule about-rule"></div>
<p class="abs about-tag">Lawyers Serving the Big Island and Neighboring Islands</p>
<p class="abs about-copy" style="top:409px">Nullam nec tincidunt elit. In egestas, dolor sed hendrerit accumsan, mauris enim lobortis ante, id porta augue massa id elit. Duis suscipit ipsum quis mi posuere, non auctor risus elementum. Pellentesque aliquet faucibus libero. Aliquam in sapien viverra, fermentum sem vitae, dignissim libero.</p>
<p class="abs about-copy" style="top:460px">Vestibulum sed neque vel nulla vulputate gravida. Phasellus id aliquam purus, id elementum dolor. Interdum et malesuada fames ac ante ipsum primis in faucibus.</p>
<div class="abs btn-red">KNOW MORE</div>

<svg class="abs practice" width="708" height="231" viewBox="0 546 708 231" role="img" aria-label="Black and white photo of a laughing child, dimmed behind the practice areas">
  <defs><linearGradient id="practiceShade" x1="0" x2="1"><stop offset="0" stop-color="#5e5e5e"/><stop offset=".5" stop-color="#4a4a4a"/><stop offset="1" stop-color="#3e3e3e"/></linearGradient></defs>
  <polygon points="0,546 356,574 708,546 708,776 356,754 0,776" fill="url(#practiceShade)"/>
</svg>
<div class="abs portrait" role="img" aria-label="Portrait photo of the lead attorney in a dark suit"></div>

<h2 class="abs h-section practice-title">OUR PRACTICE AREA</h2>
<div class="abs rule practice-rule"></div>
<div class="abs area" style="left:136px">
  <svg width="40" height="40" viewBox="0 0 40 40"><circle cx="20" cy="20" r="19" stroke="#fff" stroke-width="1.2" fill="none"/><path d="M11 20L20 12L29 20M14 18V28H26V18M17 24L23 20" stroke="#fff" stroke-width="1.3" fill="none"/></svg>CRIMINAL LAW</div>
<div class="abs area" style="left:238px">
  <svg width="40" height="40" viewBox="0 0 40 40"><circle cx="20" cy="20" r="19" stroke="#fff" stroke-width="1.2" fill="none"/><path d="M12 12L15 15M15 12L12 15M24 25L27 28M27 25L24 28M14 20Q20 14 26 16M23 14L26 16L24 19" stroke="#fff" stroke-width="1.2" fill="none"/><circle cx="15" cy="26" r="1.5" fill="#fff"/><circle cx="27" cy="13" r="1.5" fill="#fff"/></svg>BANKRUPTCY LAW</div>
<div class="abs area" style="left:347px">
  <svg width="40" height="40" viewBox="0 0 40 40"><circle cx="20" cy="20" r="19" stroke="#fff" stroke-width="1.2" fill="none"/><circle cx="20" cy="14" r="4" stroke="#fff" stroke-width="1.2" fill="none"/><path d="M13 29Q13 20 20 20Q27 20 27 29M18 22L20 29L22 22" stroke="#fff" stroke-width="1.2" fill="none"/></svg>PERSONAL INJURY LAW</div>
<div class="abs area" style="left:457px">
  <svg width="40" height="40" viewBox="0 0 40 40"><circle cx="20" cy="20" r="19" stroke="#fff" stroke-width="1.2" fill="none"/><path d="M17 11L25 19M14 14L22 22M15.5 12.5L23.5 20.5M20 17L28 25M12 28H24" stroke="#fff" stroke-width="1.4" fill="none"/></svg>FAMILY LAW</div>
<div class="abs dots"><i class="on"></i><i></i><i></i><i></i><i></i></div>

<h2 class="abs h-section team-title">OUR ATTORNEYS</h2>
<div class="abs rule team-rule"></div>
<div class="abs arrow" style="left:113px"><svg width="6" height="8" viewBox="0 0 6 8"><path d="M5 1L2 4L5 7" stroke="#fff" stroke-width="1.6" fill="none"/></svg></div>
<div class="abs arrow" style="left:577px"><svg width="6" height="8" viewBox="0 0 6 8"><path d="M1 1L4 4L1 7" stroke="#fff" stroke-width="1.6" fill="none"/></svg></div>
<article class="abs card" style="left:147px"><div class="card-photo" role="img" aria-label="Photo of attorney Peter L. Arundel"></div><div class="card-name">PETER L. ARUNDEL</div><div class="card-role">Managing Partner</div></article>
<article class="abs card" style="left:254px"><div class="card-photo" role="img" aria-label="Photo of attorney Clara Venn" style="background:linear-gradient(160deg,#d8cfc4,#3a3532)"></div><div class="card-name">Clara Venn</div><div class="card-role">Senior Partner</div></article>
<article class="abs card" style="left:359px"><div class="card-photo" role="img" aria-label="Photo of attorney Owen Hartley" style="background:linear-gradient(160deg,#9aa2a8,#2c3138)"></div><div class="card-name">OWEN HARTLEY</div><div class="card-role">Partner( Head of Litigation)</div></article>
<article class="abs card" style="left:465px"><div class="card-photo" role="img" aria-label="Photo of attorney Nathan Brierly" style="background:linear-gradient(160deg,#cfd6dc,#1f2329)"></div><div class="card-name">Nathan Brierly</div><div class="card-role">Partner ( Head of<br>Business Developments)</div></article>

<footer>
  <section class="abs foot-info">
    <div class="office">LAw Office of MARCUS PELLOW</div>
    <dl>
      <dt>Find Us</dt><dd>48-2210 Palani Road, Suite 310<br>Hilo, Hawaii 96720.</dd>
      <dt>Call Us Today</dt><dd>T:&nbsp;&nbsp;+1.808.555.0142</dd>
      <dt>Email Us Now</dt><dd>info@marcuspellow.com</dd>
      <dt>Visit Our Website</dt><dd>www.marcuspellow.com</dd>
    </dl>
    <div class="foot-social"><i style="background:#3b5a9a"></i><i style="background:#2aa3e0"></i><i style="background:#1a78b4"></i></div>
  </section>
  <section class="abs contact">
    <h2>CONTACT US</h2>
    <div class="field" style="top:42px">Name</div>
    <div class="field" style="top:60px">Email</div>
    <div class="field" style="top:77px">Phone</div>
    <div class="field" style="top:96px;height:32px">Message</div>
    <div class="submit">SUBMIT</div>
  </section>
  <section class="abs map" role="img" aria-label="Street map of the office location along the coast"></section>
  <div class="abs copyright">Copyright © 2019, Law offcie of Marcus Pellow. All Rights Reserved.</div>
</footer>

</body>
</html>
```